Buch-/E-Book-Cover Pathways to Hire & Charm the Locals
Klares Design und rasche Umsetzung aller Änderungswünsche. Vielen Dank, gerne wieder.
Zielgruppe
Ich helfe internationalen Fachkräften Jobs in Deutschland zu finden. Meine Zielgruppe ist hochgebildet (97% mit Uni-Abschluss), spricht fließend englisch, ist global mobil und kommt aus allen Teilen der Welt.
Das PROBLEM MEINER ZIELGRUPPE:
Trotz hervorragender Fähigkeiten scheitert meine Zielgruppe im normalen Bewerbungsprozess. Der Grund: Sie werden nicht als individuelle Person, als Mensch mit Fähigkeiten bewertet - sondern nur als STEREOTYP gesehen. Ich helfe meinen Klienten in ein direktes Gespräch mit den Entscheidern einzutreten - damit sie wieder als einzelner Mensch, als Profi bewertet werden.
Aufgabenstellung
UPDATE: Ich habe ein neues Foto für die Rückseite hochgeladen. Morgen (Donnerstag) sende ich die verschiedenen Entwürfe zum Voting an meine Zielgruppe. Ich hoffe das ich dann innerhalb weniger Tage die Siegerin oder den Sieger bestimmen kann. :)
Aktualisierte Neuauflage meines englischsprachigen Buches 'Pathways to Hire & Charm the Locals'. Buchumschlag design für Verlora BPX Paperback und Hardcover.
Beide Formate sind in den Abmessungen identisch:
Paperback 13,97 x 21,59 cm
Hardcover 13,97 x 21,59 cm
UPDATE: Das Buch hat 159 Seiten.
Die 'Third updated Edition' sollte evtl. in einem Störer hervorgehoben werden.
Das Design muss aus der Masse der Verlora Titel hervorstechen - auch dann wenn man es auf einem Smartphone betrachtet. Das Design soll klar und modern sein. Ich prüfe bei jedem Design ob es zwischen diesen Suchresultaten auffallen würde:
https://www.verlora-shop.de/gp/toplist/books/582913/ref=vx_tl_qrbs_books
Würde ich dieses Buchcover anklicken?
Meine Zielgruppe verdient oberhalb von 60.000€ jährlich. Meine Dienstleistung (Coaching) ist entsprechend teuer. Am Besten denken Designer darüber nach wie über ein *Luxusprodukt* - dass dem Kunden aber gleichzeitig ein höheres Einkommen sichert.
Buchtitel: Pathways to Hire & Charm the Locals
Untertitel: The Newcomers' Manual for Working Abroad Well
Störer oder Teil des Untertitels: Third & Updated Edition
Author: Dana Owerk
Das Verlagslogo füge ich unten in zwei Versionen bei.
WICHTIG: Der Buchumschlag muss allen Verlora BPX Anforderungen entsprechen. (Z.B. Platz für barcode auf der Rückseite etc.) - Designs die diesen Anforderungen nicht entsprechen, scheiden automatisch aus.
Ansonsten habe ich keine Vorgaben.
Weitere Infos:
Klappentext - Rückseite:
German angst rules HR departments and destroys career opportunities for international talent and everyone else who dar..

```html
<!DOCTYPE html>
<html lang="en">
<head>
<meta charset="utf-8">
<title>Pathways to Hire &amp; Charm the Locals – Cover</title>
<link rel="stylesheet" href="https://fonts.googleapis.com/css2?family=Bebas+Neue&family=Oswald:wght@500&family=Roboto+Condensed:wght@500;700&family=PT+Serif:wght@400;700&display=swap">
<style>
  :root {
    --stage: #e4e4e2;
    --paper: #ffffff;
    --ink: #25282c;
    --red: #e5322b;
    --yellow: #e8dc2e;
    --body-ink: #2a2a2a;
    --photo-light: #f1f1f1;
    --photo-mid: #dcdcdc;
  }
  * { box-sizing: border-box; margin: 0; padding: 0; }
  html, body { width: 1200px; height: 861px; overflow: hidden; }
  body { background: var(--stage); position: relative; }

  .cover {
    position: absolute;
    top: 50px;
    width: 492px;
    height: 760px;
    background: var(--paper);
    overflow: hidden;
  }
  .cover--back { left: 80px; }
  .cover--front { left: 628px; }

  /* Back cover */
  .back-copy {
    position: absolute;
    top: 0; left: 0; right: 0;
    padding: 34px 40px 0;
    font-family: "PT Serif", serif;
    color: var(--body-ink);
    font-size: 12px;
    line-height: 1.28;
    text-align: justify;
  }
  .back-title {
    font-weight: 700;
    font-size: 19px;
    line-height: 1.2;
    text-align: center;
    margin-bottom: 20px;
    color: var(--ink);
  }
  .back-copy .source { margin-bottom: 3px; }
  .back-copy .author-heading { margin: 14px 0 10px; }
  .back-photo {
    position: absolute;
    left: 0; right: 0; bottom: 0;
    height: 140px;
    background: linear-gradient(90deg, #1f1f1f 0%, #2a2a2a 22%, #d8271f 34%, #e0342a 52%, #e9d92a 64%, #f0e03a 80%, var(--photo-light) 100%);
  }

  /* Front cover */
  .edition-badge {
    position: absolute;
    top: 22px; left: 50%;
    transform: translateX(-50%);
    background: var(--yellow);
    color: var(--paper);
    font-family: "Oswald", sans-serif;
    font-weight: 500;
    font-size: 22px;
    letter-spacing: 0.01em;
    padding: 2px 14px;
    white-space: nowrap;
  }
  .title {
    position: absolute;
    top: 70px; left: 0; right: 0;
    text-align: center;
    font-family: "Bebas Neue", sans-serif;
    font-weight: 400;
    line-height: 0.86;
  }
  .title-line { display: block; }
  .title-lead { font-size: 108px; color: var(--ink); }
  .title-hire { font-size: 94px; color: var(--red); }
  .title-hire .amp { color: var(--ink); font-size: 80px; }
  .title-charm { font-size: 112px; color: var(--yellow); }
  .title-locals {
    font-size: 54px;
    color: var(--ink);
    letter-spacing: 0.55em;
    margin-right: -0.55em;
    margin-top: 6px;
  }
  .front-photo {
    position: absolute;
    left: 0; right: 0;
    top: 445px; height: 240px;
    background: linear-gradient(180deg, var(--paper) 0%, var(--photo-light) 45%, var(--photo-mid) 100%);
  }
  .subtitle {
    position: absolute;
    top: 692px; left: 0; right: 0;
    text-align: center;
    font-family: "Roboto Condensed", sans-serif;
    font-weight: 500;
    font-size: 15.5px;
    color: var(--ink);
    text-transform: uppercase;
  }
  .author {
    position: absolute;
    top: 722px; left: 0; right: 0;
    text-align: center;
    font-family: "Roboto Condensed", sans-serif;
    font-weight: 700;
    font-size: 20px;
    letter-spacing: 0.04em;
    color: var(--ink);
  }
</style>
</head>
<body>

<section class="cover cover--back" aria-label="Back cover">
  <div class="back-photo" role="img" aria-label="Photo of black, red and yellow game pawns standing in a row"></div>
  <div class="back-copy">
    <h2 class="back-title">Pathways to Hire &amp; Charm the Locals</h2>
    <p>German angst rules HR departments and destroys career opportunities for international talent and everyone else who dares to be “different”. Dana Owerk explains step by step how international professionals overcome prejudice and get the jobs they deserve. “Pathways to Hire &amp; Charm the Locals” will help you build a career by being a person and not a tool. This is the third updated edition.</p>
    <p>“Dana Owerk advises international professionals on how to enter the job market. To this end, he has written a book entitled ‘Pathways to Hire &amp; Charm the Locals’. His conclusion: Germany has a poor reputation among international professionals.”</p>
    <p class="source">Rundblick</p>
    <p>“Germany has a shortage of around 400,000 skilled workers, yet only 4 percent of German companies hire new employees who do not speak German. That has to change, demands career coach Dana Owerk.”</p>
    <p class="source">Leitwerk Magazin</p>
    <p>“Germany urgently needs international skilled workers. Companies should therefore also hire English-speaking candidates and offer them language courses, demands Dana Owerk.”</p>
    <p class="source">Tagesbote</p>
    <p class="author-heading">The Author</p>
    <p>Dana Owerk introduces international professionals to employers in Germany. Since 2013 Dana has helped over 300 professionals find their next job in his home country. If you are an expert who doesn’t (want) to fit into an imaginary “ISO-norm”, Dana is your best ally.</p>
    <p>As an expert on immigration and international careers, he is often quoted by German quality media from Rundblick to Tagesbote. He worked in five different cultures and lived in five countries. After ten years back home, Dana Owerk moved with his family to the North of Spain.</p>
  </div>
</section>

<section class="cover cover--front" aria-label="Front cover">
  <div class="edition-badge">THIRD &amp; UPDATED EDITION</div>
  <h1 class="title">
    <span class="title-line title-lead">PATHWAYS TO</span>
    <span class="title-line title-hire">HIRE <span class="amp">&amp;</span></span>
    <span class="title-line title-charm">CHARM THE</span>
    <span class="title-line title-locals">LOCALS</span>
  </h1>
  <div class="front-photo" role="img" aria-label="Photo of black, red and yellow game pawns beside a drawn circle, with a die in front"></div>
  <p class="subtitle">The Newcomers' Manual for Working Abroad Well</p>
  <p class="author">DANA OWERK</p>
</section>

</body>
</html>
```